Label Design For Vitamin C Serum for Larkwind Skin Care

I need a label design for a bottle similar to this:

https://www.tradelumo-market.example/item/Sample-Face-Serum-Bottle/50000000001.html

Industry/Entity Type

Skin Care Product

Font styles to use
Other font styles liked:
• use logo and use anything standard for label text

Colors
000000

Requirements
Must have
• 20% Vitamin C Brightening Serum
• 30 ML
• On back of label:
• Vitamin C serum is a potent antioxidant designed to help minimize the damaging effects of free oxygen radicals.
• This formulation will help restore skin tone and youthful appearance to the skin.
• Apply 2-3 drops of serum to desired areas. Massage with fingertips.
Nice to have
• I want to use the GOLD LOGO with BLACK LABEL

```html
<!DOCTYPE html>
<html lang="en">
<head>
<meta charset="utf-8">
<title>Larkwind Skin Care – Vitamin C Serum Label</title>
<link rel="stylesheet" href="https://fonts.googleapis.com/css2?family=Montserrat:wght@400;500&family=Roboto+Condensed:ital,wght@0,400;1,400&display=swap">
<style>
  :root {
    --page: #f4f2ef;
    --label: #231f20;
    --gold: #c9a045;
    --ink: #ffffff;
    --soft-ink: #e9e6e1;
    --pink: #e59bb8;
  }
  * { box-sizing: border-box; margin: 0; padding: 0; }
  html, body { width: 1033px; height: 1200px; overflow: hidden; background: var(--page); }
  .sheet {
    position: relative; width: 1033px; height: 1200px;
    display: flex; justify-content: center; align-items: center; gap: 40px;
  }
  .label {
    width: 460px; height: 640px; background: var(--label);
    color: var(--ink); position: relative;
  }

  /* Front */
  .label--front { display: flex; flex-direction: column; align-items: center; padding-top: 56px; }
  .brand {
    text-align: center; color: var(--gold);
    font-family: "Montserrat", sans-serif; font-weight: 500;
    font-size: 30px; letter-spacing: 3px; line-height: 1.3;
  }
  .product-name {
    margin-top: 62px; text-align: center;
    font-family: "Montserrat", sans-serif; font-weight: 400; line-height: 1.15;
  }
  .product-name__percent { display: block; font-size: 40px; }
  .product-name__word { display: block; font-size: 58px; }
  .product-type {
    margin-top: 70px; border: 3px solid var(--soft-ink); border-radius: 28px;
    padding: 8px 24px; font-family: "Montserrat", sans-serif;
    font-size: 28px; letter-spacing: 2px; font-weight: 500;
  }
  .volume { margin-top: 22px; font-family: "Montserrat", sans-serif; font-size: 30px; }

  /* Back */
  .label--back {
    padding: 42px 30px 0; font-family: "Roboto Condensed", sans-serif;
    color: var(--soft-ink);
  }
  .description { font-size: 25px; line-height: 1.32; text-align: justify; }
  .directions { margin-top: 18px; font-size: 23px; line-height: 1.45; text-align: center; font-style: italic; }
  .ingredients { margin-top: 18px; font-size: 22px; line-height: 1.3; text-align: justify; font-style: italic; }
  .ingredients__title { font-style: normal; text-transform: uppercase; }
  .symbols { position: absolute; left: 0; right: 0; bottom: 44px; display: flex; justify-content: space-around; align-items: center; padding: 0 40px; }
  .badge { width: 56px; height: 56px; border-radius: 50%; background: var(--pink); }
</style>
</head>
<body>
<main class="sheet">
  <section class="label label--front" aria-label="Front label">
    <div class="brand">LARKWIND<br>SKIN CARE</div>
    <div class="product-name">
      <span class="product-name__percent">20%</span>
      <span class="product-name__word">Vitamin C</span>
    </div>
    <div class="product-type">Brigtening Serum</div>
    <div class="volume">℮ 30 ml / 1 fl.oz.</div>
  </section>

  <section class="label label--back" aria-label="Back label">
    <p class="description">Vitamin C serum is a potent antioxidant designed to help minimize the damaging effects of free oxygen radicals. This formulation will help restore skin tone and youthful appearance to the skin.</p>
    <p class="directions">Apply 2-3 drops of serum to desired areas.<br>Massage with fingertips.</p>
    <p class="ingredients"><span class="ingredients__title">Ingredients:</span> Lorem ipsum dolor sit amet, consectetur adipiscing elit. Phasellus vitae consectetur eros. Pellentesque finibus quis arcu a malesuada. Quisque tristique a lectus id faucibus.</p>
    <div class="symbols">
      <div class="badge" role="img" aria-label="Cruelty-free certification badge"></div>
      <svg width="70" height="80" viewBox="0 0 70 80" role="img" aria-label="12 months after opening">
        <g fill="none" stroke="var(--soft-ink)" stroke-width="2.5">
          <path d="M14 30 L56 4"/>
          <path d="M14 30 L18 36"/>
          <rect x="10" y="40" width="50" height="36" rx="4"/>
        </g>
        <text x="35" y="66" text-anchor="middle" fill="var(--soft-ink)" font-family="Roboto Condensed, sans-serif" font-size="20">12 M</text>
      </svg>
      <svg width="64" height="64" viewBox="0 0 64 64" role="img" aria-label="Recyclable">
        <g fill="none" stroke="var(--ink)" stroke-width="7">
          <path d="M18 22 L28 8 L38 22"/>
          <path d="M48 30 L54 46 L38 50"/>
          <path d="M24 54 L8 48 L14 32"/>
        </g>
      </svg>
    </div>
  </section>
</main>
</body>
</html>
```